Payroll Brochure

Create a brochure with the copy i have provided . A simple easy tp read brochure that shows wat we do we handle payroll taxes insurance 401k etc

```html
<!DOCTYPE html>
<html lang="en">
<head>
<meta charset="UTF-8">
<title>The NWP Advantage – Payroll Brochure Cover</title>
<link rel="stylesheet" href="https://fonts.googleapis.com/css2?family=Libre+Baskerville:wght@400;700&family=Open+Sans:wght@400;600&display=swap">
<style>
  :root {
    --backdrop: #8f8f8f;
    --paper: #ffffff;
    --maroon: #6e0b0b;
    --brown: #9c4a22;
    --bronze: #b87a3a;
    --gold: #e2b84f;
    --pale-gold: #f3dc86;
    --ink: #161616;
    --muted: #444444;
  }
  * { margin: 0; padding: 0; box-sizing: border-box; }
  html, body { width: 1200px; height: 900px; overflow: hidden; }
  body {
    background: var(--backdrop);
    font-family: "Open Sans", sans-serif;
    position: relative;
  }
  .cover {
    position: absolute;
    left: 290px;
    top: 20px;
    width: 620px;
    height: 860px;
    background: var(--paper);
    overflow: hidden;
  }
  .cover-shapes {
    position: absolute;
    inset: 0;
    width: 620px;
    height: 860px;
  }
  .team-photo {
    position: absolute;
    left: 110px;
    top: 125px;
    width: 370px;
    height: 370px;
    border-radius: 50%;
    border: 11px solid var(--maroon);
    box-shadow: 0 0 0 8px var(--paper);
    background:
      linear-gradient(180deg, rgba(255,255,255,0) 0%, rgba(255,255,255,0) 45%, rgba(40,30,28,0.55) 100%),
      linear-gradient(90deg, #d9c2ad 0%, #f2ece6 30%, #ece4dc 55%, #e6c9c4 80%, #cdb29a 100%);
  }
  .brand-mark {
    position: absolute;
    left: 160px;
    top: 178px;
    display: flex;
    align-items: center;
    gap: 10px;
  }
  .brand-mark .brand-square {
    width: 38px;
    height: 38px;
    background: var(--bronze);
  }
  .brand-mark .brand-name {
    font-family: "Libre Baskerville", serif;
    font-weight: 700;
    font-size: 42px;
    color: var(--maroon);
    line-height: 1;
  }
  .headline {
    position: absolute;
    left: 150px;
    top: 600px;
    font-family: "Libre Baskerville", serif;
    color: var(--ink);
    line-height: 1;
  }
  .headline .headline-lead {
    font-size: 30px;
    font-weight: 400;
  }
  .headline .headline-brand {
    font-size: 44px;
    font-weight: 700;
    color: var(--maroon);
  }
  .headline .headline-main {
    display: block;
    font-size: 46px;
    font-weight: 400;
    margin-top: 4px;
    margin-left: 30px;
  }
  .tagline {
    position: absolute;
    left: 150px;
    top: 716px;
    font-size: 9.5px;
    color: var(--muted);
  }
  .website {
    position: absolute;
    left: 0;
    right: 0;
    top: 812px;
    text-align: center;
    font-size: 15px;
    font-weight: 600;
    letter-spacing: 5px;
    color: var(--paper);
  }
</style>
</head>
<body>
  <main class="cover">
    <svg class="cover-shapes" viewBox="0 0 620 860" aria-hidden="true">
      <defs>
        <linearGradient id="panelFill" x1="0" y1="0" x2="0.3" y2="1">
          <stop offset="0" stop-color="#9c4a22"/>
          <stop offset="0.45" stop-color="#c98f45"/>
          <stop offset="1" stop-color="#e8c35a"/>
        </linearGradient>
        <linearGradient id="bandFill" x1="0" y1="0" x2="1" y2="0">
          <stop offset="0" stop-color="#c8923f"/>
          <stop offset="1" stop-color="#9c4a22"/>
        </linearGradient>
        <linearGradient id="stripeFill" x1="0" y1="0" x2="1" y2="1">
          <stop offset="0" stop-color="#f3dc86"/>
          <stop offset="1" stop-color="#d9a74a"/>
        </linearGradient>
      </defs>
      <polygon class="stripe" points="0,190 290,80 320,80 0,215" fill="url(#stripeFill)" opacity="0.85"/>
      <polygon class="stripe" points="0,250 180,180 170,200 0,268" fill="#f3dc86" opacity="0.7"/>
      <polygon class="stripe" points="30,330 100,545 118,545 48,330" fill="url(#stripeFill)" opacity="0.8"/>
      <polygon class="stripe" points="70,550 240,592 240,606 70,564" fill="#d9a74a" opacity="0.85"/>
      <polygon class="panel" points="330,60 550,60 620,160 620,460 510,580 270,580 270,500" fill="url(#panelFill)"/>
      <polygon class="panel-edge" points="530,592 620,490 620,512 548,592" fill="#f3dc86"/>
      <polygon class="accent-bar" points="470,778 620,748 620,770 470,800" fill="url(#bandFill)" opacity="0.9"/>
      <polygon class="footer-band" points="0,798 620,770 620,860 0,860" fill="url(#bandFill)"/>
    </svg>

    <div class="team-photo" role="img" aria-label="Group photo of smiling office colleagues standing together"></div>

    <div class="brand-mark">
      <span class="brand-square"></span>
      <span class="brand-name">NWP</span>
    </div>

    <h1 class="headline">
      <span class="headline-lead">THE</span>
      <span class="headline-brand">NWP</span>
      <span class="headline-main">Advantage</span>
    </h1>

    <p class="tagline">developed a comprehensive suite of products and services that will fit your needs</p>

    <p class="website">www.yourwebsite.com</p>
  </main>
</body>
</html>
```